Mobile (Android/iPhone) game studio needs stationary design and a business card

We are Plunk Ferret Software and we need a fun and creative stationary design. Our company builds Android and iPhone games and children's software. The stationary designs should reflect an entertainment, fun and creativity. The pieces of stationary we need are:
1. A4 and Letter Word template (company letterhead)
2. A4 and Letter PPT template
3. Business card
4. Envelopes of various standard sizes
Each of the designs should somehow utilize our company logo.
The business card should have the following:
1. Incorporates our company logo (see attached)
2. Has a front and back with the same design (front is English, back is Traditional Chinese)
3. Delivered in an editable template so we can easily add new business cards using the same template when we hire more employees
4. Field for full name
5. Field for employee's title
6. Field for employee's email address
7. Field for company phone number - +886-2-51384470
8. Field for mobile phone number
9. Field for company fax number - +886-2-51384492
10. Company website address: www.plunkferret.example
11. Company address (on English side): 7F-2, NO. 63, Lane 91, Guoyuan Road, Dali District, Taipei Taiwan
12. Company address (on Traditional Chinese side): See Word document attachment for address in Chinese characters
Industry/Entity Type
Games
Look and feel
Each slider illustrates characteristics of the customer's brand and the style your logo design should communicate.

```html
<!DOCTYPE html>
<html lang="en">
<head>
<meta charset="utf-8">
<title>Plunk Ferret Software – Business Card</title>
<link href="https://fonts.googleapis.com/css2?family=Arimo:wght@400;700&family=Noto+Sans+TC:wght@400&display=swap" rel="stylesheet">
<style>
  :root {
    --page-bg: #f4f5f7;
    --card-bg: #ffffff;
    --band-top: #35a8e6;
    --band-bottom: #0a5fb4;
    --brand-blue: #1f86d2;
    --label-cyan: #27a7e2;
    --text-grey: #5e5e5e;
    --name-white: #ffffff;
    --card-edge: #e2e4e8;
  }
  * { margin: 0; padding: 0; box-sizing: border-box; }
  html, body { width: 1200px; height: 395px; overflow: hidden; }
  body {
    background: var(--page-bg);
    font-family: "Arimo", Arial, sans-serif;
    position: relative;
  }
  .card {
    position: absolute;
    top: 62px;
    width: 505px;
    height: 280px;
    background: var(--card-bg);
    border: 1px solid var(--card-edge);
    border-radius: 22px;
    overflow: hidden;
  }
  .card--english { left: 80px; }
  .card--chinese { left: 615px; }

  .band-stub, .name-band {
    position: absolute;
    top: 58px;
    height: 53px;
    background: linear-gradient(to bottom, var(--band-top), var(--band-bottom));
  }
  .band-stub { left: 0; width: 32px; }
  .name-band { left: 175px; right: 0; padding: 11px 0 0 18px; color: var(--name-white); }
  .employee-name { font-size: 14.5px; font-weight: 400; line-height: 17px; }
  .employee-title { font-size: 12px; font-weight: 700; line-height: 16px; margin-top: 2px; }

  .brand {
    position: absolute;
    left: 32px;
    top: 44px;
    width: 143px;
    text-align: center;
  }
  .brand-mark { display: block; margin: 0 auto 6px; }
  .brand-name {
    color: var(--brand-blue);
    font-size: 12px;
    font-weight: 700;
    line-height: 14px;
  }

  .details {
    position: absolute;
    left: 193px;
    color: var(--text-grey);
    font-size: 12px;
    line-height: 15px;
  }
  .phones { top: 130px; }
  .label { color: var(--label-cyan); }
  .web { top: 189px; }
  .address { top: 232px; }
  .address--zh {
    font-family: "Noto Sans TC", "Arimo", sans-serif;
    font-size: 12px;
    top: 238px;
    left: 190px;
  }
</style>
</head>
<body>

<section class="card card--english" aria-label="Business card, English side">
  <div class="band-stub"></div>
  <div class="brand">
    <svg class="brand-mark" width="40" height="40" viewBox="0 0 40 40" aria-hidden="true">
      <circle cx="20" cy="20" r="19" fill="#1f86d2"/>
    </svg>
    <div class="brand-name">Plunk Ferret<br>Software</div>
  </div>
  <div class="name-band">
    <div class="employee-name">Marcus Ellery</div>
    <div class="employee-title">Sales Representative</div>
  </div>
  <div class="details phones">
    <div><span class="label">T:</span> 02 5138 4470</div>
    <div><span class="label">F:</span> 02 5138 4492</div>
    <div><span class="label">M:</span> 0912 604 318</div>
  </div>
  <div class="details web">
    <div>marcus@plunkferret.example</div>
    <div>www.plunkferret.example</div>
  </div>
  <div class="details address">
    <div>7F-2, NO. 63, Lane 91, Guoyuan Road,</div>
    <div>Dali District, Taipei Taiwan</div>
  </div>
</section>

<section class="card card--chinese" lang="zh-Hant" aria-label="Business card, Traditional Chinese side">
  <div class="band-stub"></div>
  <div class="brand">
    <svg class="brand-mark" width="40" height="40" viewBox="0 0 40 40" aria-hidden="true">
      <circle cx="20" cy="20" r="19" fill="#1f86d2"/>
    </svg>
    <div class="brand-name" lang="en">Plunk Ferret<br>Software</div>
  </div>
  <div class="name-band" lang="en">
    <div class="employee-name">Marcus Ellery</div>
    <div class="employee-title">Sales Representative</div>
  </div>
  <div class="details phones" lang="en">
    <div><span class="label">T:</span> 02 5138 4470</div>
    <div><span class="label">F:</span> 02 5138 4492</div>
    <div><span class="label">M:</span> 0912 604 318</div>
  </div>
  <div class="details web" lang="en">
    <div>marcus@plunkferret.example</div>
    <div>www.plunkferret.example</div>
  </div>
  <div class="details address address--zh">台灣台北市大理區國園路91巷63號7樓之2</div>
</section>

</body>
</html>
```